Corvid Aviation - Learn to Fly

Our customers are people who span all ages and genders that are interested in learning how to fly airplanes for fun or as a career, or who would like to advance their piloting skills.

Flight training we offer:
Private Pilot Certificate
Instrument Rating
Commercial Pilot Certificate
Sport Pilot Certificate: Powered Parachute
Drone Pilot Training

Ground School we offer:
Sport Pilot Ground School
Private Pilot Ground School
Instrument Pilot Ground School
Drone Pilot Ground School

Target Market(s)

Bessemer, Alabama, United States: High school students, college students, career changers. Someone interested in learning to fly for fun or for a career in the United States.

Industry/Entity Type

Aviation

Requirements
Must have
• I would like for you to enjoy some creative freedom here. The feeling and image we want to portray is a professional, but also very exciting and energizing image. The prospective customer and student should see the brochure and be excited to call us or come out for more information on learning how to fly. Our tag line is: "Small Step Today, Giant Leap Tomorrow."
Nice to have
• It would be helpful if you can do some reading or a little research on each of the types of training that we offer so that you will understand what should be included in the brochure. Our goal is to let everyone know who we are, what we offer, and how to contact us.

This may help some with design ideas: The name Corvid Aviation is inspired by the Orbix Skyward space program because the owner of the flight school is a big fan of Orbix and the Skyward mission.

```html
<!DOCTYPE html>
<html lang="en">
<head>
<meta charset="utf-8">
<title>Corvid Aviation – Learn to Fly</title>
<link rel="stylesheet" href="https://fonts.googleapis.com/css2?family=Anton&family=Oswald:wght@400;500;600&family=Roboto:wght@400;500;700&display=swap">
<style>
  :root{
    --navy:#17203a;
    --navy-deep:#0f1629;
    --red:#e1252b;
    --yellow:#f4e22c;
    --white:#ffffff;
    --paper:#f1f2f4;
    --ink:#2a2f3d;
    --grey:#6b7080;
    --rule:#c9ccd3;
  }
  *{margin:0;padding:0;box-sizing:border-box}
  html,body{width:849px;height:1200px;overflow:hidden;background:var(--paper)}
  .flyer{position:relative;width:849px;height:1200px;overflow:hidden;background:var(--paper);font-family:'Roboto',sans-serif}
  .backdrop,.hero-photo{position:absolute;left:0;top:0}
  .headline{position:absolute;left:46px;top:128px;font-family:'Anton',sans-serif;color:var(--yellow);font-size:96px;line-height:0.98;letter-spacing:1px}
  .brand-mark{position:absolute;left:330px;top:400px;width:210px;height:210px;border-radius:50%;background:var(--white);border:10px solid var(--navy);display:flex;align-items:center;justify-content:center;text-align:center}
  .brand-name{font-family:'Oswald',sans-serif;font-weight:600;font-size:28px;line-height:1.1;color:var(--navy);letter-spacing:1px}
  .col-heading{font-family:'Oswald',sans-serif;font-weight:400;font-size:32px;line-height:1.05;letter-spacing:.5px}
  .flight-training{position:absolute;left:46px;top:640px;width:360px;color:var(--ink)}
  .flight-training .col-heading{color:var(--grey)}
  .course-list{list-style:none;margin-top:20px}
  .flight-training li{display:flex;align-items:flex-start;gap:12px;padding:9px 0;border-bottom:1px solid var(--rule);font-size:19px;line-height:1.2}
  .cert-icon{flex:none;width:22px;height:18px;margin-top:2px}
  .ground-school{position:absolute;left:470px;top:612px;width:340px;color:var(--white)}
  .ground-school li{display:flex;align-items:center;gap:12px;padding:11px 0;font-size:19px;line-height:1.2;border-bottom:1px solid rgba(255,255,255,.15)}
  .dot{flex:none;width:13px;height:13px;border-radius:50%;background:var(--red)}
  .call-to-action{position:absolute;left:0;top:1012px;width:849px;text-align:center}
  .cta-line{font-family:'Oswald',sans-serif;font-weight:600;color:var(--yellow);font-size:33px;line-height:1.12;letter-spacing:.5px}
  .tagline{margin-top:8px;font-family:'Roboto',sans-serif;font-weight:700;font-style:italic;color:var(--white);font-size:19px}
  .contact-bar{position:absolute;left:0;top:1118px;width:849px;height:82px;background:var(--red);display:flex;align-items:center;padding:0 40px;color:var(--white)}
  .phone{display:flex;align-items:center;gap:12px;font-family:'Oswald',sans-serif;font-weight:600;font-size:36px;letter-spacing:1px;width:390px}
  .phone svg{width:40px;height:40px}
  .contact-group{display:flex;flex-direction:column;gap:6px;font-size:13px;width:200px}
  .contact-row{display:flex;align-items:center;gap:7px}
  .contact-row svg{width:14px;height:14px;flex:none}
</style>
</head>
<body>
<main class="flyer">
  <svg class="backdrop" width="849" height="1200" viewBox="0 0 849 1200" aria-hidden="true">
    <rect width="849" height="1200" fill="var(--paper)"/>
    <path d="M300 640 C420 600 560 560 849 500 L849 1000 L300 1000 C380 900 400 760 300 640 Z" fill="var(--navy)"/>
    <rect x="0" y="1000" width="849" height="120" fill="var(--navy)"/>
  </svg>

  <svg class="hero-photo" width="849" height="640" viewBox="0 0 849 640" role="img" aria-label="Photo of a pilot and student seated beside a small aircraft under a dark evening sky">
    <defs>
      <linearGradient id="sky" x1="0" y1="0" x2="0.4" y2="1">
        <stop offset="0" stop-color="#2d3e5e"/>
        <stop offset="0.55" stop-color="#3a4a63"/>
        <stop offset="1" stop-color="#1c2438"/>
      </linearGradient>
    </defs>
    <path d="M0 0 H849 V420 C620 440 360 470 0 560 Z" fill="url(#sky)"/>
    <path d="M0 560 C360 470 620 440 849 420 V470 C620 500 360 540 0 630 Z" fill="var(--red)"/>
    <path d="M0 630 C360 540 620 500 849 470 V500 C620 530 380 570 0 640 Z" fill="var(--white)"/>
  </svg>

  <h1 class="headline">LEARN<br>TO FLY</h1>

  <div class="brand-mark"><span class="brand-name">CORVID<br>AVIATION</span></div>

  <section class="flight-training">
    <h2 class="col-heading">FLIGHT TRAINING<br>WE OFFER:</h2>
    <ul class="course-list">
      <li><svg class="cert-icon" viewBox="0 0 22 18"><rect x="1" y="1" width="20" height="13" rx="1" fill="var(--red)"/><rect x="4" y="4" width="10" height="2" fill="#fff"/><rect x="4" y="8" width="7" height="2" fill="#fff"/><circle cx="16" cy="14" r="3" fill="var(--red)" stroke="#fff" stroke-width="1"/></svg>Private Pilot Certificate</li>
      <li><svg class="cert-icon" viewBox="0 0 22 18"><rect x="1" y="1" width="20" height="13" rx="1" fill="var(--red)"/><rect x="4" y="4" width="10" height="2" fill="#fff"/><rect x="4" y="8" width="7" height="2" fill="#fff"/><circle cx="16" cy="14" r="3" fill="var(--red)" stroke="#fff" stroke-width="1"/></svg>Instrument Rating</li>
      <li><svg class="cert-icon" viewBox="0 0 22 18"><rect x="1" y="1" width="20" height="13" rx="1" fill="var(--red)"/><rect x="4" y="4" width="10" height="2" fill="#fff"/><rect x="4" y="8" width="7" height="2" fill="#fff"/><circle cx="16" cy="14" r="3" fill="var(--red)" stroke="#fff" stroke-width="1"/></svg>Commercial Pilot Certificate</li>
      <li><svg class="cert-icon" viewBox="0 0 22 18"><rect x="1" y="1" width="20" height="13" rx="1" fill="var(--red)"/><rect x="4" y="4" width="10" height="2" fill="#fff"/><rect x="4" y="8" width="7" height="2" fill="#fff"/><circle cx="16" cy="14" r="3" fill="var(--red)" stroke="#fff" stroke-width="1"/></svg>Sport Pilot Certificate:<br>Powered Parachute</li>
      <li><svg class="cert-icon" viewBox="0 0 22 18"><rect x="1" y="1" width="20" height="13" rx="1" fill="var(--red)"/><rect x="4" y="4" width="10" height="2" fill="#fff"/><rect x="4" y="8" width="7" height="2" fill="#fff"/><circle cx="16" cy="14" r="3" fill="var(--red)" stroke="#fff" stroke-width="1"/></svg>Drone Pilot Training</li>
    </ul>
  </section>

  <section class="ground-school">
    <h2 class="col-heading">GROUND SCHOOL<br>WE OFFER:</h2>
    <ul class="course-list">
      <li><span class="dot"></span>Sport Pilot Ground School</li>
      <li><span class="dot"></span>Private Pilot Ground School</li>
      <li><span class="dot"></span>Instrument Pilot Ground School</li>
      <li><span class="dot"></span>Drone Pilot Ground School</li>
    </ul>
  </section>

  <section class="call-to-action">
    <p class="cta-line">GET INTOUCH WITH US TO START<br>LEARNING HOW TO FLY</p>
    <p class="tagline">"Small Step Today, Giant Leap Tomorrow."</p>
  </section>

  <footer class="contact-bar">
    <div class="phone">
      <svg viewBox="0 0 40 40"><circle cx="20" cy="20" r="18" fill="none" stroke="#fff" stroke-width="2.5"/><path d="M14 11 l4 0 2 6 -3 2 c1.5 3 3 4.5 6 6 l2-3 6 2 0 4 c-1 1.5 -3 2 -5 1.5 -7-2 -12-7 -14-14 -0.5-2 0-4 2-4.5z" fill="#fff"/></svg>
      000-000-00-00
    </div>
    <div class="contact-group">
      <span class="contact-row"><svg viewBox="0 0 14 14"><circle cx="7" cy="7" r="6" fill="none" stroke="#fff" stroke-width="1.3"/><path d="M1 7h12M7 1c-3 3-3 9 0 12M7 1c3 3 3 9 0 12" fill="none" stroke="#fff" stroke-width="1"/></svg>www.yourwebsite.com</span>
      <span class="contact-row"><svg viewBox="0 0 14 14"><rect x="1" y="3" width="12" height="8" fill="none" stroke="#fff" stroke-width="1.3"/><path d="M1 3l6 5 6-5" fill="none" stroke="#fff" stroke-width="1.3"/></svg>email@yourwebsite.com</span>
    </div>
    <div class="contact-group">
      <span class="contact-row"><svg viewBox="0 0 14 14"><path d="M7 13C3 8 2 6.5 2 5a5 5 0 0 1 10 0c0 1.5-1 3-5 8z" fill="#fff"/><circle cx="7" cy="5" r="1.8" fill="var(--red)"/></svg>Your business location here</span>
    </div>
  </footer>
</main>
</body>
</html>
```